Create a Big Data Website that is professional but has a creative flare to it.

I am after a modern business design for a company in the Big Data space however it still needs to have a wow value and something stand out from other corporate websites.
My competitors websites are to give you and idea of content:
www.fendralux.com
www.vornuby.com
www.quillmerq4.com.au
www.tessovant.com
I have uploaded my company Logo so you can use that to make sure it matches your theme.

Target Market(s)

Banks, Insurance Companies, Government, Gas and Energy Companies and Food Manufacturing.

Industry/Entity Type

Consulting

Number of Pages Required

5+ page

Colors

Designer to choose colors to be used in the design.

Requirements
Must have
• Images, Diagrams around Big Data. Usage of information or graphs from sources like Pellwick are fine to use.
Nice to have
• Interactive design use mouse overs, change in text, highlighting information for clear focus.
Should not have
• Cluttered Pages of Informaiton

```html
<!DOCTYPE html>
<html lang="en">
<head>
<meta charset="utf-8">
<title>Meridane Consulting Services</title>
<link rel="stylesheet" href="https://fonts.googleapis.com/css2?family=Open+Sans:wght@400;600;700&display=swap">
<style>
:root{
  --blue:#0a8fd8;
  --blue-dark:#0b7cc0;
  --navy:#1b3a6b;
  --ink:#333a44;
  --text:#4a4f57;
  --muted:#6b7079;
  --grey-band:#e9eaec;
  --grey-news:#efefef;
  --white:#ffffff;
}
*{margin:0;padding:0;box-sizing:border-box}
html,body{width:1200px;height:2601px;overflow:hidden}
body{font-family:"Open Sans",Arial,sans-serif;color:var(--text);background:var(--white);position:relative}
.abs{position:absolute}

/* header */
.site-header{position:absolute;left:0;top:0;width:1200px;height:121px;background:var(--white)}
.brand{position:absolute;left:99px;top:30px;display:flex;align-items:center;gap:14px}
.brand-dot{width:46px;height:46px;border-radius:50%;background:var(--blue)}
.brand-name{font-weight:700;font-size:34px;color:var(--navy);line-height:1}
.brand-sub{font-weight:600;font-size:13px;letter-spacing:2.4px;color:var(--blue);margin-top:4px}
.call{position:absolute;right:118px;top:46px;font-weight:700;font-size:21px;color:var(--ink);display:flex;align-items:center;gap:12px}

/* nav */
.main-nav{position:absolute;left:0;top:121px;width:1200px;height:56px;background:var(--blue)}
.main-nav ul{list-style:none;display:flex;position:absolute;left:140px;top:0;height:56px;align-items:center;gap:0}
.main-nav li{color:var(--white);font-size:14px;font-weight:600;margin-right:43px}
.nav-search{position:absolute;right:124px;top:16px}

/* hero */
.hero{position:absolute;left:0;top:177px;width:1200px;height:449px;
  background:radial-gradient(circle at 40% 30%,#1f8aa8 0%,#0d4d6e 25%,#06233b 55%,#020b16 100%)}
.hero-kicker{position:absolute;left:0;width:1200px;top:133px;text-align:center;color:var(--white);font-size:16px;font-weight:600}
.hero-title{position:absolute;left:0;width:1200px;top:160px;text-align:center;color:var(--white);font-size:58px;font-weight:700;letter-spacing:1px}
.hero-arrow{position:absolute;top:161px;width:48px;height:52px;display:flex;align-items:center;justify-content:center}
.hero-arrow.prev{left:100px}
.hero-arrow.next{left:1053px;background:rgba(40,40,40,.85)}
.hero-badge{position:absolute;left:559px;top:564px;width:82px;height:82px;border-radius:50%;background:var(--blue);border:5px solid var(--white)}

/* section headings */
.section-title{position:absolute;left:0;width:1200px;text-align:center;font-weight:700;color:var(--ink);letter-spacing:4px;font-size:22px}
.rule{position:absolute;left:572px;width:56px;height:3px;background:var(--navy)}

.welcome-lead{position:absolute;left:0;width:1200px;top:722px;text-align:center;font-size:16px;color:var(--text)}
.welcome-body{position:absolute;left:190px;width:820px;top:760px;text-align:center;font-size:12.3px;line-height:20.5px;color:var(--muted)}
.btn{position:absolute;background:var(--blue);color:var(--white);font-size:12.5px;font-weight:600;display:flex;align-items:center;justify-content:center}

/* topics */
.topic{position:absolute;width:240px;text-align:center}
.topic-circle{width:116px;height:116px;border-radius:50%;margin:0 auto;display:flex;align-items:center;justify-content:center}
.topic-circle.navy{background:var(--navy)}
.topic-circle.blue{background:var(--blue)}
.topic-title{font-weight:600;font-size:16px;color:var(--ink);margin-top:36px}
.topic-text{font-size:12.5px;line-height:20px;color:var(--muted);margin-top:6px}
.dots{position:absolute;top:1250px;left:586px;display:flex;gap:10px}
.dots span{width:8px;height:8px;border-radius:50%;background:var(--navy)}
.dots span+span{background:var(--blue)}

/* audiences */
.audience{position:absolute;width:420px;height:80px}
.audience svg{position:absolute;left:0;top:-4px}
.audience h3{position:absolute;left:90px;top:0;font-size:16px;font-weight:600;color:var(--ink)}
.audience p{position:absolute;left:90px;top:30px;width:280px;font-size:12.5px;line-height:20px;color:var(--muted);text-align:justify}

/* reports */
.reports{position:absolute;left:0;top:1786px;width:1200px;height:500px;background:var(--grey-band)}
.reports-art{position:absolute;left:90px;top:87px;width:597px;height:343px;border-radius:14px 14px 6px 6px;
  background:linear-gradient(160deg,#2b2f36 0%,#3a3f47 60%,#c9ccd1 100%)}
.reports-rule{position:absolute;left:706px;top:162px;width:56px;height:3px;background:var(--navy)}
.reports-title{position:absolute;left:706px;top:184px;width:420px;font-size:22px;font-weight:700;letter-spacing:4px;line-height:32px;color:var(--ink)}
.reports-sub{position:absolute;left:706px;top:252px;width:420px;font-size:25px;line-height:33px;color:var(--text)}

/* newsletter */
.newsletter{position:absolute;left:0;top:2286px;width:1200px;height:197px;background:var(--grey-news)}
.newsletter-title{position:absolute;left:0;width:1200px;top:38px;text-align:center;font-size:22px;letter-spacing:4px;color:var(--ink)}
.email-field{position:absolute;left:333px;top:100px;width:352px;height:36px;background:var(--white);display:flex;align-items:center;padding:0 20px;font-size:12px;letter-spacing:2px;color:#b0b3b8;justify-content:space-between}
.subscribe{left:697px;top:100px;width:170px;height:36px;font-size:16px;font-weight:400}

/* footer */
.site-footer{position:absolute;left:0;top:2483px;width:1200px;height:118px;background:var(--white)}
.footer-brand{position:absolute;left:99px;top:20px;display:flex;align-items:center;gap:10px}
.footer-brand .brand-dot{width:34px;height:34px}
.footer-brand .brand-name{font-size:26px}
.footer-brand .brand-sub{font-size:10px;letter-spacing:1.8px}
.footer-nav{position:absolute;right:96px;top:30px;list-style:none;display:flex;gap:0}
.footer-nav li{font-size:12px;color:var(--ink);margin-left:38px}
.copyright{position:absolute;right:98px;top:63px;font-size:11px;color:var(--ink)}
.social{position:absolute;left:101px;top:72px;display:flex;gap:12px}
.social span{width:26px;height:26px;border-radius:3px}
</style>
</head>
<body>

<header class="site-header">
  <div class="brand">
    <div class="brand-dot"></div>
    <div>
      <div class="brand-name">meridane</div>
      <div class="brand-sub">CONSULTING SERVICES</div>
    </div>
  </div>
  <div class="call">
    <svg width="18" height="18" viewBox="0 0 18 18"><rect x="0" y="0" width="18" height="18" rx="3" fill="#333a44"/><path d="M5 4c1 0 2 2 2 3s-1 1-1 1.5 1.5 3 3 3.5c.5 0 .5-1 1.5-1s3 1 3 2-1 2-2 2C8 15 3 10 3 6c0-1 1-2 2-2z" fill="#fff"/></svg>
    Call Us : 1-800 555 0142
  </div>
</header>

<nav class="main-nav">
  <ul>
    <li>HOME</li><li>ABOUT US</li><li>RESEARCH</li><li>EVENTS</li><li>ANALYSTS</li><li>CONSULTING</li><li>CONTACT US</li>
  </ul>
  <svg class="nav-search" width="22" height="22" viewBox="0 0 22 22"><circle cx="9" cy="9" r="6.5" fill="none" stroke="#fff" stroke-width="2.6"/><line x1="14" y1="14" x2="20" y2="20" stroke="#fff" stroke-width="3" stroke-linecap="round"/></svg>
</nav>

<section class="hero" role="img" aria-label="Glowing digital globe made of data points and network lines">
  <div class="hero-kicker">WE PROVIDE SERVICES</div>
  <div class="hero-title">BIG DATA</div>
  <div class="hero-arrow prev"><svg width="12" height="18" viewBox="0 0 12 18"><path d="M9 2 3 9l6 7" fill="none" stroke="#fff" stroke-width="2.5"/></svg></div>
  <div class="hero-arrow next"><svg width="12" height="18" viewBox="0 0 12 18"><path d="M3 2l6 7-6 7" fill="none" stroke="#fff" stroke-width="2.5"/></svg></div>
</section>
<div class="hero-badge"></div>

<h2 class="section-title" style="top:667px">WELCOME TO MERIDANE CONSULTING SERVICES</h2>
<div class="rule" style="top:712px"></div>
<p class="welcome-lead">Sed ut perspiciatis unde omnis iste natus error sit voluptatem...</p>
<p class="welcome-body">Sed ut perspiciatis unde omnis iste natus error sit voluptatem accusantium doloremque laudantium, totam rem aperiam, eaque ipsa quae ab illo inventore veritatis et quasi architecto beatae vitae dicta sunt explicabo. Nemo enim ipsam voluptatem quia voluptas sit aspernatur aut odit aut fugit, sed quia consequuntur magni dolores eos qui ratione voluptatem sequi nesciunt. Neque porro quisquam est, qui dolorem ipsum quia dolor sit amet, consectetur, adipisci velit, sed quia non numquam eius modi tempora incidunt ut labore et dolore magnam aliquam quaerat voluptatem.</p>
<div class="btn" style="left:549px;top:861px;width:103px;height:32px">READ MORE</div>

<h2 class="section-title" style="top:918px">EXPLORE TRENDING TOPICS</h2>
<div class="rule" style="top:961px"></div>

<div class="topic" style="left:109px;top:1012px">
  <div class="topic-circle navy">
    <svg width="64" height="60" viewBox="0 0 64 60" fill="none" stroke="#fff" stroke-width="2.2"><rect x="6" y="6" width="52" height="36"/><line x1="2" y1="6" x2="62" y2="6"/><polyline points="12,34 22,24 30,30 40,18 50,22"/><line x1="32" y1="42" x2="32" y2="50"/><line x1="32" y1="50" x2="22" y2="58"/><line x1="32" y1="50" x2="42" y2="58"/></svg>
  </div>
  <div class="topic-title">Trends &amp; Predictions</div>
  <div class="topic-text">Predictions for 2017: Innovation Brings<br>Digital Disruption</div>
</div>
<div class="topic" style="left:360px;top:1012px">
  <div class="topic-circle blue">
    <svg width="66" height="62" viewBox="0 0 66 62"><g fill="#fff" font-family="Open Sans, sans-serif" font-weight="700" font-size="19"><text x="12" y="18">100</text><text x="4" y="38">1010</text><text x="12" y="58">01</text></g></svg>
  </div>
  <div class="topic-title">Data Analytics</div>
  <div class="topic-text">Advance Your Business with Advanced<br>Analytics</div>
</div>
<div class="topic" style="left:610px;top:1012px">
  <div class="topic-circle navy">
    <svg width="66" height="60" viewBox="0 0 66 60" fill="none" stroke="#fff" stroke-width="2.2"><path d="M16 38h36a10 10 0 0 0 0-20 16 16 0 0 0-30-4A12 12 0 0 0 16 38z"/><line x1="24" y1="38" x2="24" y2="52"/><line x1="33" y1="38" x2="33" y2="56"/><line x1="42" y1="38" x2="42" y2="52"/><circle cx="24" cy="54" r="2"/><circle cx="33" cy="57" r="2"/><circle cx="42" cy="54" r="2"/></svg>
  </div>
  <div class="topic-title">Cloud Computing</div>
  <div class="topic-text">5 Ways Cloud Can Transform Your<br>Business</div>
</div>
<div class="topic" style="left:855px;top:1012px">
  <div class="topic-circle blue">
    <svg width="62" height="58" viewBox="0 0 62 58" fill="none" stroke="#fff" stroke-width="2.2"><rect x="6" y="4" width="50" height="34"/><rect x="12" y="10" width="38" height="22"/><line x1="31" y1="38" x2="31" y2="46"/><rect x="14" y="46" width="34" height="8"/></svg>
  </div>
  <div class="topic-title">Internet Of Things</div>
  <div class="topic-text">Why IoT? Harness the Power of<br>Connected Things</div>
</div>
<div class="dots"><span></span><span></span></div>

<h2 class="section-title" style="top:1320px">YOUR SOURCE FOR TECHNOLOGY RESEARCH AND INSIGHT</h2>
<div class="rule" style="top:1374px"></div>

<div class="audience" style="left:130px;top:1426px">
  <svg width="76" height="70" viewBox="0 0 76 70"><polygon points="20,4 56,4 72,35 56,66 20,66 4,35" fill="none" stroke="#1b3a6b" stroke-width="8"/><circle cx="38" cy="28" r="7" fill="none" stroke="#0a8fd8" stroke-width="2.5"/><path d="M26 48c0-8 6-11 12-11s12 3 12 11z" fill="none" stroke="#0a8fd8" stroke-width="2.5"/></svg>
  <h3>CIOs and IT Executives</h3>
  <p>Maximize technology investments and drive business results</p>
</div>
<div class="audience" style="left:690px;top:1426px">
  <svg width="76" height="70" viewBox="0 0 76 70"><polygon points="20,4 56,4 72,35 56,66 20,66 4,35" fill="none" stroke="#0a8fd8" stroke-width="8"/><circle cx="38" cy="26" r="7" fill="none" stroke="#1b3a6b" stroke-width="2.5"/><path d="M26 50c0-9 6-14 12-14s12 5 12 14z" fill="none" stroke="#1b3a6b" stroke-width="2.5"/></svg>
  <h3>IT Professionals</h3>
  <p>Amplify business performance through IT</p>
</div>
<div class="audience" style="left:130px;top:1530px">
  <svg width="76" height="70" viewBox="0 0 76 70"><polygon points="20,4 56,4 72,35 56,66 20,66 4,35" fill="none" stroke="#1b3a6b" stroke-width="8"/><rect x="24" y="24" width="28" height="20" fill="none" stroke="#0a8fd8" stroke-width="2.5"/><line x1="24" y1="30" x2="52" y2="30" stroke="#0a8fd8" stroke-width="2"/><circle cx="46" cy="42" r="5" fill="#fff" stroke="#0a8fd8" stroke-width="2.5"/></svg>
  <h3>Digital Marketing Professionals</h3>
  <p>Real-time, personalized digital marketing guidance, from vision through execution</p>
</div>
<div class="audience" style="left:690px;top:1530px">
  <svg width="76" height="70" viewBox="0 0 76 70"><polygon points="20,4 56,4 72,35 56,66 20,66 4,35" fill="none" stroke="#0a8fd8" stroke-width="8"/><circle cx="34" cy="38" r="8" fill="none" stroke="#1b3a6b" stroke-width="3" stroke-dasharray="4 2"/><circle cx="46" cy="27" r="5" fill="none" stroke="#1b3a6b" stroke-width="2.5" stroke-dasharray="3 2"/></svg>
  <h3>Professional Services</h3>
  <p>Customer, competitor and market intelligence to grow your business</p>
</div>
<div class="audience" style="left:130px;top:1634px">
  <svg width="76" height="70" viewBox="0 0 76 70"><polygon points="20,4 56,4 72,35 56,66 20,66 4,35" fill="none" stroke="#1b3a6b" stroke-width="8"/><path d="M28 24c2 0 4 4 4 6s-2 2-2 3 3 6 6 7c1 0 1-2 3-2s5 2 5 4-2 4-4 4c-9 0-18-9-18-18 0-2 2-4 6-4z" fill="none" stroke="#0a8fd8" stroke-width="2.5"/></svg>
  <h3>High-Tech &amp; Telecom Professionals</h3>
  <p>Compete more effectively, increase share and grow market leadership</p>
</div>
<div class="audience" style="left:690px;top:1634px">
  <svg width="76" height="70" viewBox="0 0 76 70"><polygon points="20,4 56,4 72,35 56,66 20,66 4,35" fill="none" stroke="#0a8fd8" stroke-width="8"/><circle cx="38" cy="35" r="5" fill="#1b3a6b"/><g fill="none" stroke="#1b3a6b" stroke-width="2"><circle cx="38" cy="21" r="4"/><circle cx="38" cy="49" r="4"/><circle cx="24" cy="35" r="4"/><circle cx="52" cy="35" r="4"/></g></svg>
  <h3>Supply Chain Professionals</h3>
  <p>Deliver excellent customer service amid demand fluctuations</p>
</div>

<section class="reports">
  <div class="reports-art" role="img" aria-label="Laptop showing a circular four-step business diagram: investigation, planning, goals and sales"></div>
  <div class="reports-rule"></div>
  <h2 class="reports-title">LEARN ABOUT OUR SPECIAL REPORTS</h2>
  <p class="reports-sub">Stay informed of emerging trends, technologies and innovations.</p>
  <div class="btn" style="left:711px;top:331px;width:103px;height:33px">READ MORE</div>
</section>

<section class="newsletter">
  <h2 class="newsletter-title">NEWSLETTER SUBSCRIBE</h2>
  <div class="email-field"><span>ENTER EMAIL ID</span>
    <svg width="14" height="10" viewBox="0 0 14 10"><rect x="1" y="1" width="12" height="8" fill="none" stroke="#555" stroke-width="1.5"/><polyline points="1,1 7,6 13,1" fill="none" stroke="#555" stroke-width="1.5"/></svg>
  </div>
  <div class="btn subscribe">SUBSCRIBE</div>
</section>

<footer class="site-footer">
  <div class="footer-brand">
    <div class="brand-dot"></div>
    <div>
      <div class="brand-name">meridane</div>
      <div class="brand-sub">CONSULTING SERVICES</div>
    </div>
  </div>
  <ul class="footer-nav">
    <li>HOME</li><li>ABOUT US</li><li>RESEARCH</li><li>EVENTS</li><li>ANALYSTS</li><li>CONSULTING</li><li>CONTACT US</li>
  </ul>
  <div class="copyright">© 2017 www.meridane.com &nbsp;|&nbsp; All Rights Reserved.</div>
  <div class="social">
    <span style="background:#3b5998"></span><span style="background:#29a9e1"></span><span style="background:#6a9a3b"></span><span style="background:#8a6a4a"></span>
  </div>
</footer>

</body>
</html>
```